Brightfernrx website

We are a weight loss clinic and we need a website built. please look at these websites for content and style. Just need like 5 pages see samples. AI files of logo are not avail yet so use sample for place set

https://glowshiftstudio.com/
ortanvital.com
https://pinecrestclinicalbodybalance.com/
https://yourslimmingnook.com/
https://qrvskinstudio.com/treatments/weight-loss-injections/

Target Market(s)

Women

Industry/Entity Type

weight loss

Coding

Coded - Design and coding required

Number of Pages Required

5+ page

Requirements
Nice to have
• please make look like a medspa website

```html
<!DOCTYPE html>
<html lang="en">
<head>
<meta charset="utf-8">
<title>Brightfernrx — Weight Loss Clinic</title>
<link href="https://fonts.googleapis.com/css2?family=Cinzel:wght@400;600&family=Poppins:ital,wght@0,400;0,500;0,600;1,400&display=swap" rel="stylesheet">
<style>
:root{
  --green:#86b05a;
  --green-dark:#6f9a45;
  --blue:#3aaed6;
  --blue-head:#3a9cc8;
  --ink:#1f2a2e;
  --muted:#444;
  --hero-bg:#eef6f3;
  --soft-green:#eef3e6;
  --footer-bg:#f1f8f9;
  --grad:linear-gradient(90deg,#3aaed6,#86b05a);
}
*{box-sizing:border-box;margin:0;padding:0}
html,body{width:1200px;height:4498px;overflow:hidden}
body{font-family:'Poppins',sans-serif;color:var(--ink);background:#fff;position:relative}
.abs{position:absolute}
section,header,footer,.topbar{position:absolute;left:0;width:1200px}
.serif{font-family:'Cinzel',serif}
.btn{position:absolute;display:flex;align-items:center;justify-content:center;border-radius:20px;font-size:13px;color:#fff;background:var(--grad)}
.btn-outline{background:#fff;color:var(--ink);border:1.5px solid var(--blue)}
.mark{position:absolute;left:585px;width:30px;height:30px;border-radius:50%;background:var(--grad)}
.sec-title{position:absolute;left:0;width:1200px;text-align:center;font-family:'Cinzel',serif;font-size:33px;color:var(--ink)}
.sec-title .hl{color:var(--blue-head)}
.ph{position:absolute}

.topbar{top:0;height:35px;background:var(--green);color:#fff;font-size:12px;display:flex;align-items:center;justify-content:center}

header{top:35px;height:78px}
.logo{position:absolute;display:flex;align-items:center;gap:10px;font-family:'Poppins',sans-serif;font-weight:600;font-size:26px;color:var(--green-dark)}
.logo i{display:block;width:34px;height:34px;border-radius:50%;background:var(--blue)}
.phone{left:800px;top:23px;display:flex;align-items:center;gap:10px;font-size:13px;font-weight:600}
.phone span.ring{width:36px;height:36px;border:1.5px solid var(--green);border-radius:50%;display:flex;align-items:center;justify-content:center}
.menu{left:1114px;top:28px;width:26px}
.menu b{display:block;height:2px;background:var(--blue);margin-bottom:7px;border-radius:2px}
.menu b:nth-child(2){width:18px;margin-left:8px}

.hero{top:35px;height:655px;background:linear-gradient(120deg,#f3f8f4,#e4f2f5 60%,#f2f7ee);z-index:-1}
.hero-title{left:61px;top:200px;font-family:'Cinzel',serif;font-size:50px;line-height:56px;color:var(--ink);font-weight:600}
.hero-title .hl{color:var(--blue-head)}
.hero-text{left:61px;top:350px;width:560px;font-size:13px;line-height:22px}
.ring-big{position:absolute;border:4px solid;border-color:var(--blue) var(--blue) var(--green) var(--green);border-radius:50%}
.dots{left:578px;top:590px;display:flex;gap:9px;align-items:center}
.dots i{width:8px;height:8px;border-radius:50%;background:#111;display:block}
.dots i.on{width:12px;height:12px;background:#fff;border:2px solid var(--blue)}

.about{top:690px;height:503px}
.about h2{top:140px;font-size:33px;line-height:42px;font-variant:small-caps}
.about p{left:280px;top:230px;width:640px;text-align:center;font-size:13.5px;line-height:22.5px;color:var(--muted)}

.program{top:1193px;height:487px;background:linear-gradient(90deg,#82ac57,#8bb660)}
.program h2{left:630px;top:100px;font-family:'Cinzel',serif;font-size:32px;line-height:42px;color:#fff;font-variant:small-caps}
.program p{left:630px;top:185px;width:500px;font-size:13px;line-height:22.5px;color:#fff}

.treatments{top:1680px;height:530px;background:var(--soft-green)}
.card{position:absolute;top:198px;width:250px;height:269px;border-radius:6px;overflow:hidden}
.card .img{height:230px}
.card .lbl{height:39px;background:var(--green);color:#fff;font-family:'Cinzel',serif;font-size:14px;display:flex;align-items:center;justify-content:center;gap:6px}

.beauty{top:2210px;height:501px}
.beauty h2{left:61px;top:165px;font-family:'Cinzel',serif;font-size:34px;color:var(--ink)}
.beauty h2 .hl{color:var(--blue-head)}
.beauty p{left:61px;top:220px;width:500px;font-size:13px;line-height:22.5px;color:var(--muted)}

.reviews{top:2711px;height:428px;background:linear-gradient(90deg,#3db2d8,#43b4d6)}
.reviews h2{color:#fff;top:130px;font-size:32px}
.stars{left:0;width:1200px;top:182px;text-align:center;color:#f5d22a;font-size:22px;letter-spacing:3px}
.reviews p{left:300px;top:225px;width:600px;text-align:center;color:#fff;font-style:italic;font-size:13px;line-height:22.5px}
.reviews .name{left:0;width:1200px;top:350px;text-align:center;color:#fff;font-family:'Cinzel',serif;font-size:13px}

.results{top:3139px;height:687px}
.results h2{top:135px;font-variant:small-caps}
.results .cap{position:absolute;top:200px;font-family:'Cinzel',serif;font-size:14px}
.pair{position:absolute;top:227px;height:304px;display:flex;gap:0;border-radius:8px;overflow:hidden}
.pair .ph{position:relative;flex:1}
.pair .divider{width:3px;background:var(--green)}

.newsletter{top:3826px;height:310px;background:linear-gradient(90deg,#86b05a,#8eb862)}
.newsletter h2{color:#fff;top:62px;font-size:32px}
.newsletter .sub{left:0;width:1200px;top:112px;text-align:center;color:#fff;font-style:italic;font-size:13px}
.field{position:absolute;top:148px;width:271px;height:36px;background:#fff;border-radius:18px;font-size:13px;display:flex;align-items:center;padding-left:20px}

footer{top:4136px;height:362px;background:var(--footer-bg)}
footer h4{position:absolute;top:55px;font-family:'Cinzel',serif;font-weight:400;font-size:14px}
.hours{left:335px;top:88px;font-size:12px;line-height:25px}
.contact{left:610px;top:88px;font-size:12px;line-height:20px}
.contact div{display:flex;gap:10px;margin-bottom:14px}
.social{left:889px;top:91px;display:flex;gap:15px}
.social i{width:28px;height:28px;border-radius:50%;border:1.5px solid var(--ink);display:block}
.social i:first-child{background:var(--green);border-color:var(--green)}
.copy{left:0;width:1200px;top:329px;border-top:1px solid var(--blue);padding-top:14px;text-align:center;font-size:12px}
.copy b{color:var(--blue-head);font-weight:500}
</style>
</head>
<body>

<div class="topbar">Join for free today and get 20% off all weight loss accessibility programs.</div>

<div class="hero" role="presentation"></div>
<header>
  <div class="logo" style="left:61px;top:18px"><i></i>Brightfernrx</div>
  <div class="abs phone"><span class="ring"><svg width="16" height="16" viewBox="0 0 24 24" fill="none" stroke="#1f2a2e" stroke-width="2"><path d="M5 3h4l2 5-2.5 1.5a11 11 0 0 0 6 6L16 13l5 2v4a2 2 0 0 1-2 2A17 17 0 0 1 3 5a2 2 0 0 1 2-2z"/></svg></span>123 456 7890</div>
  <div class="btn" style="left:962px;top:23px;width:121px;height:35px">Book Online</div>
  <div class="abs menu"><b></b><b></b><b></b></div>
</header>

<div class="ring-big" style="left:727px;top:231px;width:412px;height:412px"></div>
<div class="ph" role="img" aria-label="Smiling woman in white sportswear holding a measuring tape around her waist" style="left:760px;top:130px;width:440px;height:560px;background:linear-gradient(180deg,#e9dfd6,#d9c3b0);border-radius:200px 200px 0 0;opacity:.85"></div>
<h1 class="abs hero-title">FAST AND AFFORDABLE<br><span class="hl">WEIGHT LOSS</span> CLINIC</h1>
<p class="abs hero-text">Lorem Ipsum is simply dummy text of the printing and typesetting industry. Lorem Ipsum has been the industry's standard dummy text</p>
<div class="btn" style="left:61px;top:419px;width:239px;height:35px">Start Your Weight Loss Journy</div>
<div class="btn btn-outline" style="left:61px;top:465px;width:239px;height:36px">Start Your Wellness Journy</div>
<div class="abs dots"><i></i><i class="on"></i><i></i></div>

<section class="about">
  <div class="mark" style="top:80px"></div>
  <h2 class="sec-title">How Old You Are is Your Business -<br><span class="hl">How Young You Look</span> is Our Business</h2>
  <p class="abs">Lorem Ipsum is simply dummy text of the printing and typesetting industry. Lorem Ipsum has been the industry's standard dummy text ever since the 1500s, when an unknown printer took a galley of type and scrambled it to make a type specimen book. It has survived not only five centuries, but also the leap into electronic typesetting, remaining essentially unchanged.</p>
  <div class="btn" style="left:505px;top:342px;width:188px;height:35px">Book An Appointment</div>
</section>

<section class="program">
  <h2 class="abs">Medically Supervised Weight<br>Loss Program</h2>
  <p class="abs">Lorem Ipsum is simply dummy text of the printing and typesetting industry. Lorem Ipsum has been the industry's standard dummy text ever since the 1500s, when an unknown printer took a galley of type and scrambled it to make a type specimen book. It has survived not only five centuries, but also the leap into electronic typesetting, remaining essentially unchanged.</p>
  <div class="btn" style="left:629px;top:330px;width:136px;height:35px">View Our Plans</div>
</section>
<div class="ph" role="img" aria-label="Happy slim woman in white sports underwear with outline and arrows showing a slimmer waist" style="left:130px;top:1118px;width:400px;height:562px;background:linear-gradient(180deg,#e8d9cc,#d4bda8);border-radius:180px 180px 0 0;opacity:.9"></div>

<section class="treatments">
  <div class="mark" style="top:84px"></div>
  <h2 class="sec-title" style="top:134px">OUR <span class="hl">TREATMENT</span> SERVICES</h2>
  <div class="card" style="left:61px"><div class="img" role="img" aria-label="Woman touching her clear facial skin" style="background:linear-gradient(180deg,#e3d5d0,#d8c3b9)"></div><div class="lbl">SKIN <span>⟶</span></div></div>
  <div class="card" style="left:337px"><div class="img" role="img" aria-label="Smiling woman holding her face with both hands" style="background:linear-gradient(180deg,#f2efec,#e4d6cc)"></div><div class="lbl">FACE <span>⟶</span></div></div>
  <div class="card" style="left:613px"><div class="img" role="img" aria-label="Woman looking over her bare shoulder" style="background:linear-gradient(180deg,#e6e4e1,#d6c3b6)"></div><div class="lbl">BODY <span>⟶</span></div></div>
  <div class="card" style="left:889px"><div class="img" role="img" aria-label="Woman jogging on a path beside a lake in a park" style="background:linear-gradient(180deg,#a9c48a,#8fa7a0 60%,#9a9a94)"></div><div class="lbl">WELLNESS <span>⟶</span></div></div>
</section>

<section class="beauty">
  <h2 class="abs"><span class="hl">BEAUTY</span> SERVICES</h2>
  <p class="abs">Lorem Ipsum is simply dummy text of the printing and typesetting industry. Lorem Ipsum has been the industry's standard dummy text ever since the 1500s, when an unknown printer took a galley of type and scrambled it to make a type specimen book. It has survived not only five centuries, but also the leap into electronic typesetting, remaining essentially unchanged.</p>
  <div class="btn" style="left:61px;top:352px;width:80px;height:35px">Botox</div>
  <div class="btn btn-outline" style="left:154px;top:352px;width:80px;height:35px">Fillers</div>
  <div class="btn btn-outline" style="left:246px;top:352px;width:100px;height:35px">Skincare</div>
</section>
<div class="ring-big" style="left:727px;top:2299px;width:412px;height:412px;border-bottom-color:transparent"></div>
<div class="ph" role="img" aria-label="Woman with long brown hair holding a large green monstera leaf" style="left:716px;top:2279px;width:402px;height:432px;background:linear-gradient(160deg,#d8c2b2,#c9ac98 55%,#3f6b2e);border-radius:200px 200px 0 0;opacity:.9"></div>

<section class="reviews">
  <div class="mark" style="top:70px;background:#fff"></div>
  <h2 class="sec-title">RIVIEWS FROM OUR PATIENTS</h2>
  <div class="abs stars">★★★★★</div>
  <svg class="abs" style="left:203px;top:246px" width="36" height="18" viewBox="0 0 36 18" fill="none" stroke="#fff" stroke-width="2"><path d="M35 9H2M9 2L2 9l7 7"/></svg>
  <svg class="abs" style="left:953px;top:246px" width="36" height="18" viewBox="0 0 36 18" fill="none" stroke="#fff" stroke-width="2"><path d="M1 9h33M27 2l7 7-7 7"/></svg>
  <p class="abs">Lorem Ipsum is simply dummy text of the printing and typesetting industry. Lorem Ipsum has been the industry's standard dummy text ever since the 1500s, when an unknown printer took a galley of type and scrambled it to make a type specimen book. It has survived not only five centuries, but also the leap into electronic typesetting, remaining essentially unchanged.</p>
  <div class="abs name">PATIENT NAME</div>
</section>

<section class="results">
  <div class="mark" style="top:86px"></div>
  <h2 class="sec-title">Real <span class="hl">Patients</span>, Real <span class="hl">Results</span></h2>
  <div class="cap" style="left:61px">WEIGHT LOSS</div>
  <div class="cap" style="left:618px">WEIGHT LOSS</div>
  <div class="pair" style="left:61px;width:522px">
    <div class="ph" role="img" aria-label="Waist before weight loss, mint sports top and black leggings" style="background:linear-gradient(180deg,#cfe9df 0 18%,#e2b89a 18% 70%,#1d1d1d 70%)"></div>
    <div class="divider"></div>
    <div class="ph" role="img" aria-label="Waist after weight loss, mint sports top and black leggings" style="background:linear-gradient(180deg,#cfe9df 0 18%,#e4bea2 18% 70%,#1d1d1d 70%)"></div>
  </div>
  <div class="pair" style="left:615px;width:524px">
    <div class="ph" role="img" aria-label="Waist before weight loss, grey sports top and leggings" style="background:linear-gradient(180deg,#7c7f85 0 25%,#d9a883 25% 62%,#5b5e63 62%)"></div>
    <div class="divider"></div>
    <div class="ph" role="img" aria-label="Waist after weight loss, grey sports top and leggings" style="background:linear-gradient(180deg,#7c7f85 0 25%,#d6a37d 25% 62%,#5b5e63 62%)"></div>
  </div>
  <div class="btn" style="left:500px;top:576px;width:200px;height:35px">View Our Patient Gallery</div>
</section>

<section class="newsletter">
  <h2 class="sec-title">SIGN UP OUR NEWSLATTER</h2>
  <div class="abs sub">Sign up to receive news, updates and specials in your inbox!</div>
  <div class="field" style="left:176px">First Name*</div>
  <div class="field" style="left:465px">Last Name*</div>
  <div class="field" style="left:753px">E-mail*</div>
  <div class="btn" style="left:554px;top:214px;width:89px;height:35px">Submit</div>
</section>

<footer>
  <div class="logo" style="left:61px;top:74px"><i></i>Brightfernrx</div>
  <h4 style="left:335px">OFFICE HOURS</h4>
  <div class="abs hours">Monday - 9:00 Am To 5:00 Pm<br>Tuesday - 9:00 Am To 5:00 Pm<br>Thursday - 9:00 Am To 5:00 Pm<br>Wednesday - 9:00 Am To 5:00 Pm<br>Thursday - 9:00 Am To 5:00 Pm<br>Friday - 9:00 Am To 5:00 Pm<br>Saturday - 9:00 Am To 1:00 Pm<br>Sunday - Closed</div>
  <h4 style="left:610px">CONTACT US</h4>
  <div class="abs contact">
    <div><svg width="16" height="16" viewBox="0 0 24 24" fill="none" stroke="#86b05a" stroke-width="2"><path d="M12 22s7-7 7-12a7 7 0 0 0-14 0c0 5 7 12 7 12z"/><circle cx="12" cy="10" r="2.5"/></svg><span>123 Lorem Ipsum is simply dummy<br>text of the printing.</span></div>
    <div><svg width="16" height="16" viewBox="0 0 24 24" fill="none" stroke="#86b05a" stroke-width="2"><path d="M5 3h4l2 5-2.5 1.5a11 11 0 0 0 6 6L16 13l5 2v4a2 2 0 0 1-2 2A17 17 0 0 1 3 5a2 2 0 0 1 2-2z"/></svg><span>123 456 7890</span></div>
    <div><svg width="16" height="16" viewBox="0 0 24 24" fill="none" stroke="#86b05a" stroke-width="2"><rect x="3" y="5" width="18" height="14" rx="1"/><path d="M3 6l9 7 9-7"/></svg><span>info@brightfernrx.com</span></div>
  </div>
  <h4 style="left:889px">CONNECT WITH US:</h4>
  <div class="abs social"><i aria-label="Social link"></i><i aria-label="Social link"></i><i aria-label="Social link"></i><i aria-label="Social link"></i></div>
  <div class="abs copy">Copyright © 2022 <b>BRIGHTFERNRX.</b> All rights reserved.</div>
</footer>

</body>
</html>
```